DIN A5 flyer front already exists for the sales outlet

Hi. I'd like to create a DIN A5 flyer. The front should be your design. On the back, I'd like to include more information about our business.
The back should contain (images still need to be added):
Our services
Stamps – Buying and Selling
Whether you're looking for the Lorren Swallow, classic rarities, or the latest stamp issues – we offer almost everything you need for your collection. We're happy to order any stamps we don't currently have in stock. Do you want to sell a stamp collection or have you inherited one? We offer personalized consultations and will make you a fair offer.
Coins – Buying and Selling
From historical cantonal coins and Swiss federal coins dating back to 1850, to coveted gold coins – collectors and investors will find what they're looking for with us. Whether it's a 100-franc Seraphine, rare Batzen, or the Tessin gold Seraphine – we trade with passion and expertise. We are also happy to purchase your coin collection or individual valuable pieces.
Purchase of scrap gold and precious metals
We buy scrap gold, jewelry, watches, rings, gold coins, silver coins, silver billets, silver bars, and other precious metals at fair and transparent prices. Thanks to our many years of experience, you will receive a professional appraisal and market-based purchase prices – discreetly and without obligation.
Postage service for businesses
Save on postage costs: Businesses can purchase valid postage stamps from us at a discounted rate. A simple and attractive way to permanently reduce the shipping costs of your business mail.
Visit us at our new location:
Lindenhofweg 38, 4057 Basel
Feldhaus-Brenner AG – Your specialist shop for stamps, coins and precious metals.
People who want to sell their scrap gold, stamps or coins

```html
<!DOCTYPE html>
<html lang="en">
<head>
<meta charset="utf-8">
<title>Feldhaus-Brenner AG – Our Services</title>
<link href="https://fonts.googleapis.com/css2?family=Cinzel:wght@600;700&family=Mulish:wght@400;500&display=swap" rel="stylesheet">
<style>
  :root {
    --navy: #0f1d5a;
    --navy-deep: #0a1546;
    --gold: #b8924a;
    --gold-light: #d4b06a;
    --red: #c8202f;
    --paper: #fbfbfa;
    --ink: #1b1b1f;
    --rule: #d9c49a;
  }
  * { margin: 0; padding: 0; box-sizing: border-box; }
  html, body { width: 848px; height: 1200px; overflow: hidden; background: #ffffff; }
  .flyer { position: relative; width: 848px; height: 1200px; font-family: "Mulish", sans-serif; color: var(--ink); }
  .backdrop { position: absolute; inset: 0; }
  .title {
    position: absolute; top: 58px; left: 0; width: 848px; text-align: center;
    font-family: "Cinzel", serif; font-weight: 700; font-size: 53px; letter-spacing: 0.5px; color: var(--navy);
  }
  .title .accent { color: var(--gold); }
  .title-rule { position: absolute; top: 122px; left: 207px; width: 434px; height: 14px; }
  .service { position: absolute; left: 69px; width: 710px; }
  .service-visual {
    position: absolute; left: 0; top: 0; width: 289px; border-radius: 12px;
    background: radial-gradient(ellipse at 60% 45%, #2b3a7a 0%, var(--navy-deep) 75%);
  }
  .icon-badge {
    position: absolute; left: -16px; width: 58px; height: 58px; border-radius: 50%;
    background: radial-gradient(circle at 40% 35%, var(--gold-light), var(--gold) 70%);
    border: 2px solid #f1e3c2; display: flex; align-items: center; justify-content: center;
  }
  .service-text { position: absolute; left: 313px; top: 6px; width: 370px; }
  .service-text h2 {
    font-family: "Cinzel", serif; font-weight: 700; font-size: 21px; line-height: 24px; color: var(--navy);
  }
  .service-text h2::after {
    content: ""; display: block; width: 32px; height: 2px; background: var(--gold); margin: 10px 0 10px;
  }
  .service-text p { font-size: 12.4px; line-height: 17.4px; }
  .divider { position: absolute; left: 289px; width: 421px; height: 1px; background: var(--rule); }
  .location-visual {
    position: absolute; left: 56px; top: 869px; width: 264px; height: 164px; border-radius: 12px;
    background: linear-gradient(180deg, #3d5a98 0%, #2a3d70 55%, #b0853e 100%);
  }
  .location-box {
    position: absolute; left: 318px; top: 875px; width: 467px; height: 146px; border-radius: 12px;
    background: var(--navy); text-align: center; color: #fff;
  }
  .location-box .lead { font-family: "Cinzel", serif; font-weight: 600; font-size: 18px; margin-top: 34px; padding-left: 40px; }
  .location-box .street { font-family: "Cinzel", serif; font-weight: 700; font-size: 36px; color: var(--gold-light); line-height: 44px; padding-left: 40px; }
  .location-box .city { font-family: "Cinzel", serif; font-weight: 700; font-size: 26px; padding-left: 40px; display: flex; align-items: center; justify-content: center; gap: 14px; }
  .location-box .city::before, .location-box .city::after { content: ""; width: 60px; height: 2px; background: var(--gold); }
  .pin-badge {
    position: absolute; left: 280px; top: 898px; width: 80px; height: 80px; border-radius: 50%;
    background: radial-gradient(circle at 40% 35%, var(--gold-light), var(--gold) 70%);
    border: 3px solid #f1e3c2; display: flex; align-items: center; justify-content: center;
  }
  .brand-name {
    position: absolute; left: 46px; top: 1118px; font-family: "Cinzel", serif; font-weight: 700;
    font-size: 20px; color: #ffffff; letter-spacing: 0.5px;
  }
  .tagline { position: absolute; left: 328px; top: 1107px; color: #fff; }
  .tagline strong { display: block; font-family: "Cinzel", serif; font-weight: 700; font-size: 19px; color: var(--gold-light); }
  .tagline span { font-size: 12.4px; }
  .seal {
    position: absolute; left: 689px; top: 1033px; width: 124px; height: 124px; border-radius: 50%;
    background: radial-gradient(circle at 40% 35%, #e7cd8f, var(--gold) 70%); border: 3px solid #f3e6c5;
  }
</style>
</head>
<body>
<div class="flyer">
  <svg class="backdrop" width="848" height="1200" viewBox="0 0 848 1200" aria-hidden="true">
    <rect x="18" y="16" width="812" height="1168" fill="var(--navy)"/>
    <path d="M18 95 Q380 20 830 22 L830 1040 Q420 1095 18 1005 Z" fill="var(--paper)"/>
    <path d="M18 92 Q260 34 520 34 Q300 42 18 102 Z" fill="var(--red)"/>
    <path d="M140 1045 Q460 1085 830 1038 L830 1046 Q460 1095 140 1045 Z" fill="var(--red)"/>
  </svg>

  <h1 class="title">Our <span class="accent">Services</span></h1>
  <svg class="title-rule" viewBox="0 0 434 14" aria-hidden="true">
    <line x1="0" y1="7" x2="180" y2="7" stroke="var(--navy)" stroke-width="2"/>
    <line x1="254" y1="7" x2="434" y2="7" stroke="var(--navy)" stroke-width="2"/>
    <path d="M192 7 Q205 0 217 7 Q229 14 242 7" fill="none" stroke="var(--gold)" stroke-width="2"/>
  </svg>

  <section class="service" style="top:155px;">
    <div class="service-visual" style="height:165px;" role="img" aria-label="Three classic Swiss postage stamps"></div>
    <div class="icon-badge" style="top:97px;">
      <svg width="26" height="30" viewBox="0 0 26 30"><rect x="2" y="2" width="22" height="26" fill="none" stroke="var(--navy)" stroke-width="3" stroke-dasharray="3 2"/><rect x="7" y="7" width="12" height="16" fill="var(--navy)"/></svg>
    </div>
    <div class="service-text">
      <h2>Stamps – Buying &amp; Selling</h2>
      <p>Whether you're looking for the Lorren Swallow, classic rarities, or the latest stamp issues – we offer almost everything you need for your collection. We're happy to order any stamps we don't currently have in stock. Do you want to sell a stamp collection or have you inherited one? We offer personalized consultations and will make you a fair offer.</p>
    </div>
    <div class="divider" style="top:180px;"></div>
  </section>

  <section class="service" style="top:338px;">
    <div class="service-visual" style="height:165px;" role="img" aria-label="Swiss silver and gold coins"></div>
    <div class="icon-badge" style="top:97px;">
      <svg width="30" height="28" viewBox="0 0 30 28"><g fill="var(--navy)"><ellipse cx="15" cy="22" rx="12" ry="5"/><ellipse cx="15" cy="15" rx="12" ry="5"/><ellipse cx="15" cy="8" rx="12" ry="5"/></g></svg>
    </div>
    <div class="service-text">
      <h2>Coins – Buying &amp; Selling</h2>
      <p>From historical cantonal coins and Swiss federal coins dating back to 1850, to coveted gold coins – collectors and investors will find what they're looking for with us. Whether it's a 100-franc Seraphine, rare Batzen, or the Tessin gold Seraphine – we trade with passion and expertise. We are also happy to purchase your coin collection or individual valuable pieces.</p>
    </div>
    <div class="divider" style="top:186px;"></div>
  </section>

  <section class="service" style="top:525px;">
    <div class="service-visual" style="height:171px;" role="img" aria-label="Gold jewellery, a watch, coins and a silver bar"></div>
    <div class="icon-badge" style="top:100px;">
      <svg width="30" height="26" viewBox="0 0 30 26"><g fill="var(--navy)"><path d="M9 2h12l3 9H6z"/><path d="M3 14h11l2 10H1z"/><path d="M16 14h11l2 10H14z"/></g></svg>
    </div>
    <div class="service-text">
      <h2>Purchase of Scrap Gold<br>&amp; Precious Metals</h2>
      <p>We buy scrap gold, jewelry, watches, rings, gold coins, silver coins, silver billets, silver bars, and other precious metals at fair and transparent prices. Thanks to our many years of experience, you will receive a professional appraisal and market-based purchase prices – discreetly and without obligation.</p>
    </div>
    <div class="divider" style="top:189px;"></div>
  </section>

  <section class="service" style="top:715px;">
    <div class="service-visual" style="height:132px;" role="img" aria-label="Envelopes with a priority stamp and a postage stamp"></div>
    <div class="icon-badge" style="top:62px;">
      <svg width="30" height="22" viewBox="0 0 30 22"><rect x="1" y="1" width="28" height="20" fill="var(--navy)"/><path d="M2 2 L15 12 L28 2" fill="none" stroke="var(--gold-light)" stroke-width="2"/></svg>
    </div>
    <div class="service-text">
      <h2>Postage Service for Businesses</h2>
      <p>Save on postage costs: Businesses can purchase valid postage stamps from us at a discounted rate. A simple and attractive way to permanently reduce the shipping costs of your business mail.</p>
    </div>
  </section>

  <div class="location-visual" role="img" aria-label="Basel cathedral at dusk"></div>
  <div class="location-box">
    <p class="lead">Visit us at our New Location:</p>
    <p class="street">Lindenhofweg 38</p>
    <p class="city">4057 Basel</p>
  </div>
  <div class="pin-badge">
    <svg width="30" height="42" viewBox="0 0 30 42"><path d="M15 1C7 1 1 7 1 15c0 10 14 26 14 26s14-16 14-26C29 7 23 1 15 1z" fill="#fff"/><circle cx="15" cy="15" r="5" fill="var(--gold)"/></svg>
  </div>

  <p class="brand-name">Feldhaus-Brenner</p>
  <div class="tagline">
    <strong>Feldhaus-Brenner AG –</strong>
    <span>Your specialist shop for stamps, coins and precious metals.</span>
  </div>
  <div class="seal" aria-hidden="true"></div>
</div>
</body>
</html>
```